KVRo Business Cards

We need a business card design. We are a Technology (Audio Visual) design, sales and installation company. Looking for a double sided design, clean

Contact Information for Business Card

Clean, modern look, 2 sided

Font styles to use
Sans Serif

```html
<!DOCTYPE html>
<html lang="en">
<head>
<meta charset="utf-8">
<title>KVRo Business Cards</title>
<link href="https://fonts.googleapis.com/css2?family=Lato:wght@400;700;900&display=swap" rel="stylesheet">
<style>
  :root {
    --backdrop: #e4e1de;
    --navy: #13263a;
    --orange: #e8891a;
    --paper: #f4f4f3;
    --ink: #1d2833;
  }
  * { margin: 0; padding: 0; box-sizing: border-box; }
  html, body { width: 1200px; height: 960px; overflow: hidden; }
  body {
    background: var(--backdrop);
    font-family: "Lato", sans-serif;
    position: relative;
  }
  .card {
    position: absolute;
    width: 540px;
    height: 308px;
    border-radius: 3px;
    box-shadow: 0 14px 30px rgba(0,0,0,0.14), 0 2px 6px rgba(0,0,0,0.08);
  }
  .card-front {
    left: 70px; top: 140px;
    background: var(--navy);
    display: flex; align-items: center; justify-content: center;
  }
  .card-back {
    left: 590px; top: 510px;
    background: var(--paper);
    display: flex; align-items: center;
    padding-left: 56px;
  }
  .wordmark {
    font-family: "Lato", sans-serif;
    font-weight: 900;
    font-size: 82px;
    letter-spacing: 1px;
    line-height: 1;
  }
  .card-front .wordmark { color: #f2f2f2; }
  .card-back .wordmark { color: var(--navy); font-size: 66px; }
  .divider {
    width: 2px; height: 150px;
    background: var(--orange);
    margin: 0 26px 0 34px;
  }
  .contact { color: var(--ink); font-size: 12.5px; line-height: 1.45; }
  .contact .name {
    color: var(--orange); font-weight: 700;
    font-size: 15px; letter-spacing: 0.3px; text-transform: uppercase;
  }
  .contact .role { margin-bottom: 8px; }
  .contact .address { margin-bottom: 8px; }
  .contact-line { display: flex; align-items: center; gap: 7px; }
  .contact-line svg { width: 11px; height: 11px; flex: none; }
</style>
</head>
<body>
  <section class="card card-front" aria-label="Card front">
    <span class="wordmark">KVRo</span>
  </section>

  <section class="card card-back" aria-label="Card back">
    <span class="wordmark">KVRo</span>
    <div class="divider"></div>
    <div class="contact">
      <div class="name">Daniel Reyes</div>
      <div class="role">President</div>
      <div class="address">212 Harbor Lane, Westbrook<br>OR 97, Westland</div>
      <div class="contact-line">
        <svg viewBox="0 0 12 12"><path d="M2.5 1.5l2 .3.8 2.3-1.2 1a6 6 0 0 0 2.8 2.8l1-1.2 2.3.8.3 2A1.5 1.5 0 0 1 9 11 8 8 0 0 1 1 3a1.5 1.5 0 0 1 1.5-1.5z" fill="var(--orange)"/></svg>
        000-000-000-000
      </div>
      <div class="contact-line">
        <svg viewBox="0 0 12 12"><rect x="3" y="1" width="6" height="10" rx="1" fill="none" stroke="var(--orange)" stroke-width="1.2"/></svg>
        000-000-000-000
      </div>
      <div class="contact-line">
        <svg viewBox="0 0 12 12"><rect x="1" y="2.5" width="10" height="7" fill="var(--orange)"/><path d="M1 2.5l5 4 5-4" fill="none" stroke="#fff" stroke-width="1"/></svg>
        info@websitename.com
      </div>
      <div class="contact-line">
        <svg viewBox="0 0 12 12"><circle cx="6" cy="6" r="5" fill="var(--orange)"/><path d="M1 6h10M6 1c-2.5 3-2.5 7 0 10M6 1c2.5 3 2.5 7 0 10" fill="none" stroke="#fff" stroke-width="0.8"/></svg>
        www.websitename.com
      </div>
    </div>
  </section>
</body>
</html>
```